Business Card Design

Name: Dorian Vaskell
Title : Mathematics Instructor
Dep. Department of Mathmatics

Four Tenbrook Lane
Camarillo, California 93047-2216

T: 805-552-3907
Cell: 805-219-7634

Email: dorian.vaskell047@plvnu.edu
Email: quickvaskell@zentomail.com

Reason: I don't know how to post my image on the web.

Reason: The design PDF can not be uplorded

Requirements
Must have
• http://www.plvnu.edu/tc/web/styleguide/logos-images.htm

http://www.bendleypress.com/plvnu/bc/
Nice to have
• I have to use the logo and the format based on their format to some extent.
White back ground

But is there any way to make mine special?
raised ink or 3D logo?

```html
<!DOCTYPE html>
<html lang="en">
<head>
<meta charset="utf-8">
<title>Dorian Vaskell – Business Card</title>
<link rel="stylesheet" href="https://fonts.googleapis.com/css2?family=Share+Tech+Mono&family=Open+Sans:ital,wght@1,700&family=Questrial&display=swap">
<style>
  :root {
    --card-light: #f4f4f4;
    --card-mid: #d2d2d2;
    --card-edge: #bfbfbf;
    --ring-tan: #c4b2a6;
    --mark-red: #e2332b;
    --ink: #1a1a1a;
    --ink-soft: #3a3a3a;
  }
  * { margin: 0; padding: 0; box-sizing: border-box; }
  html, body {
    width: 1200px;
    height: 703px;
    overflow: hidden;
    background: var(--card-edge);
  }
  .card {
    position: relative;
    width: 1200px;
    height: 703px;
    overflow: hidden;
    background: radial-gradient(circle at 600px 330px, var(--card-light) 0, var(--card-mid) 260px, var(--card-edge) 560px);
    color: var(--ink-soft);
    font-family: "Questrial", "Century Gothic", sans-serif;
  }
  .card-decor {
    position: absolute;
    inset: 0;
  }
  .identity {
    position: absolute;
    left: 0;
    width: 1200px;
    text-align: center;
  }
  .brand-name {
    top: 122px;
    font-size: 62px;
    letter-spacing: 6px;
    padding-left: 6px;
    color: var(--mark-red);
    font-weight: 400;
    line-height: 70px;
  }
  .name {
    top: 280px;
    font-family: "Share Tech Mono", monospace;
    font-size: 52px;
    letter-spacing: 0.5em;
    padding-left: 0.5em;
    color: var(--ink);
    font-weight: 400;
  }
  .title {
    top: 345px;
    font-family: "Open Sans", Arial, sans-serif;
    font-style: italic;
    font-weight: 700;
    font-size: 34px;
    letter-spacing: 0.5px;
    color: var(--ink);
  }
  .department {
    top: 396px;
    font-size: 30px;
    letter-spacing: 2.6px;
    padding-left: 6px;
  }
  .contact {
    position: absolute;
    left: 691px;
    top: 480px;
    font-size: 26px;
    letter-spacing: 2px;
    line-height: 34px;
  }
  .contact-heading {
    letter-spacing: 3.2px;
    margin-bottom: 15px;
  }
  .contact-emails { margin-top: 11px; }
  .address {
    position: absolute;
    left: 28px;
    top: 611px;
    font-size: 25px;
    line-height: 34px;
    font-style: normal;
  }
</style>
</head>
<body>
  <main class="card">
    <svg class="card-decor" width="1200" height="703" viewBox="0 0 1200 703" aria-hidden="true">
      <circle cx="600" cy="362" r="503" fill="none" stroke="var(--ring-tan)" stroke-width="130" opacity="0.85"/>
    </svg>

    <p class="identity brand-name">PLVNU</p>

    <h1 class="identity name">Dorian Vaskell</h1>
    <p class="identity title">Mathematics Instructor</p>
    <p class="identity department">Dep. Department of Mathmatics</p>

    <address class="address">
      Four Tenbrook Lane<br>
      Camarillo, California 93047-2216
    </address>

    <section class="contact">
      <p class="contact-heading">CONTACT:</p>
      <p>T: 805-552-3907</p>
      <p>Cell: 805-219-7634</p>
      <div class="contact-emails">
        <p>dorian.vaskell047@plvnu.edu</p>
        <p>quickvaskell@zentomail.com</p>
      </div>
    </section>
  </main>
</body>
</html>
```